Pemberly & Associates Tax Services

Need an eye catching advertisement/lead generating design for prospects interesting in professional tax planning and tax preparation services. Ideas for
Sample Advertising Language is below:

We are accepting new clients!!
We are affordable and have over 20 years of experience serving the tax needs of our clientele.

Here are a few reasons you may want to contact us:

1. You want to learn how to maximize business deductions
2. You’re a high-income earner and want to learn ways to pay less in taxes
3. You have an interest in starting a business
4. You want to maximize rental property deductions
5. You have questions about maintaining a home office
6. You want to be updated periodically on tax law changes and tax planning strategies
7. You want to be represented by a tax expert before the FRB if you are subject to an audit

References available upon request.

Target Market(s)

Individuals, small businesses and startup business

Industry/Entity Type

Tax and Accounting Industry

Requirements
Nice to have
• Would like to develop a marketing campaign that can be used periodically to digitally generate leads, build email contact list of prospective clients who want to receive tax updates.

```html
<!DOCTYPE html>
<html lang="en">
<head>
<meta charset="utf-8">
<title>Pemberly &amp; Associates – Accepting New Clients</title>
<link href="https://fonts.googleapis.com/css2?family=Roboto+Slab:wght@400;500;700&family=Lobster&display=swap" rel="stylesheet">
<style>
  :root {
    --stage: #8a8a8a;
    --blue: #1f5a9a;
    --blue-deep: #0f2f5c;
    --green: #0d9440;
    --green-light: #6cb82c;
    --ink: #1b1b1b;
    --white: #ffffff;
    --paper: #f3f3f4;
  }
  html, body { margin: 0; padding: 0; width: 1200px; height: 1200px; overflow: hidden; background: var(--stage); }
  .flyer {
    position: absolute; left: 60px; top: 219px; width: 1081px; height: 764px;
    overflow: hidden; background: var(--paper); font-family: "Roboto Slab", serif; color: var(--ink);
  }
  .flyer > * { position: absolute; }
  .backdrop { left: 0; top: 0; width: 1081px; height: 764px; }
  .team-photo {
    left: 719px; top: -5px; width: 350px; height: 350px; border-radius: 50%;
    background: radial-gradient(circle at 55% 40%, #ffffff 0%, #e9eef3 50%, #c9d2db 100%);
    border: 2px solid var(--white); box-sizing: border-box;
  }
  .headline-small { left: 65px; top: 214px; font-size: 37px; font-weight: 500; color: var(--white); margin: 0; letter-spacing: 0.5px; line-height: 44px; }
  .headline-large { left: 63px; top: 256px; font-size: 60px; font-weight: 700; color: var(--white); margin: 0; letter-spacing: 0.5px; line-height: 70px; }
  .tagline {
    left: 68px; top: 322px; width: 720px; margin: 0;
    font-family: "Lobster", cursive; color: var(--white); font-size: 19px; line-height: 38px;
  }
  .tagline .big { font-size: 31px; }
  .tagline .accent { color: var(--green-light); font-size: 27px; }
  .reasons-title { left: 69px; top: 467px; margin: 0; font-size: 29px; font-weight: 700; line-height: 36px; }
  .reasons-title span { color: var(--green); }
  .reasons-rule { left: 67px; top: 510px; width: 778px; height: 1.5px; background: var(--green); }
  .reasons { margin: 0; padding: 0; list-style: none; font-size: 13.4px; }
  .reasons li { position: relative; padding-left: 29px; height: 24.5px; line-height: 19px; white-space: nowrap; }
  .reasons svg { position: absolute; left: 0; top: 2px; width: 19px; height: 16px; }
  .reasons-left { left: 66px; top: 527px; }
  .reasons-right { left: 483px; top: 526px; }
  .reasons-right li.two-line { height: auto; line-height: 20px; }
  .cta-band { left: 0; top: 638px; width: 1081px; height: 55px; background: var(--green); color: var(--white); }
  .cta-band .references { position: absolute; left: 70px; top: 8px; margin: 0; font-size: 16px; line-height: 20px; }
  .cta-band .divider { position: absolute; left: 286px; top: 11px; width: 2px; height: 33px; background: var(--white); }
  .cta-band .campaign { position: absolute; left: 307px; top: 8px; width: 740px; margin: 0; font-size: 12.6px; line-height: 17.5px; }
  .footer { left: 0; top: 693px; width: 1081px; height: 71px; background: #f7f7f7; }
  .credential-badge { left: 69px; top: 711px; width: 56px; height: 31px; border: 3px solid #9a8c5a; box-sizing: border-box; background: #eef0f1; }
  .brand { left: 212px; top: 712px; display: flex; align-items: center; gap: 8px; }
  .brand-dot { width: 38px; height: 38px; border-radius: 50%; background: var(--blue); }
  .brand-name { font-size: 15px; font-weight: 500; color: var(--blue); line-height: 17px; }
  .services { left: 397px; top: 708px; font-size: 14.5px; margin: 0; }
  .contact-line { font-size: 14.5px; display: flex; align-items: center; gap: 6px; margin: 0; white-space: nowrap; }
  .contact-line svg { width: 12px; height: 12px; fill: var(--blue); }
  .address { left: 397px; top: 729px; }
  .phone { left: 788px; top: 707px; }
  .email { left: 788px; top: 729px; }
</style>
</head>
<body>
<main class="flyer">
  <svg class="backdrop" viewBox="0 0 1081 764">
    <defs>
      <radialGradient id="hero-glow" gradientUnits="userSpaceOnUse" cx="390" cy="140" r="430">
        <stop offset="0" stop-color="#7088b8"/>
        <stop offset="0.35" stop-color="#3a5690"/>
        <stop offset="0.7" stop-color="#1d3a6e" stop-opacity="0.6"/>
        <stop offset="1" stop-color="#1f5a9a" stop-opacity="0"/>
      </radialGradient>
    </defs>
    <rect x="0" y="0" width="1081" height="764" fill="#f3f3f4"/>
    <path d="M0 404 C300 440 700 430 1081 235 V477 C820 392 420 455 0 426 Z" fill="#5fb02c"/>
    <path d="M0 420 C400 455 800 400 1081 470 V477 C820 395 420 458 0 426 Z" fill="#2e9a35"/>
    <path d="M0 0 H1081 V222 C760 410 360 452 0 412 Z" fill="#1f5a9a"/>
    <g role="img" aria-label="Business handshake in front of a night city skyline">
      <path d="M0 0 H1081 V222 C760 410 360 452 0 412 Z" fill="url(#hero-glow)"/>
    </g>
    <circle cx="874" cy="194" r="205" fill="#1f5a9a" stroke="#ffffff" stroke-width="2"/>
  </svg>
  <div class="team-photo" role="img" aria-label="Tax advisor presenting charts to a group of clients at a meeting table"></div>

  <h2 class="headline-small">WE ARE ACCEPTING</h2>
  <h1 class="headline-large">NEW CLIENTS!!</h1>
  <p class="tagline">We are affordable and have over <span class="accent">20 years of experience</span> <span class="big">Serving the<br>tax needs of our clientele.</span></p>

  <h2 class="reasons-title">Here are a <span>few reasons</span> you may want to contact us:</h2>
  <div class="reasons-rule"></div>

  <ul class="reasons reasons-left">
    <li><svg viewBox="0 0 19 16"><path d="M1 8 L7 14 L18 1" fill="none" stroke="#1f5a9a" stroke-width="2.2"/></svg>You want to learn how to maximize business deductions</li>
    <li><svg viewBox="0 0 19 16"><path d="M1 8 L7 14 L18 1" fill="none" stroke="#1f5a9a" stroke-width="2.2"/></svg>You have an interest in starting a business</li>
    <li><svg viewBox="0 0 19 16"><path d="M1 8 L7 14 L18 1" fill="none" stroke="#1f5a9a" stroke-width="2.2"/></svg>You have questions about maintaining a home office</li>
    <li><svg viewBox="0 0 19 16"><path d="M1 8 L7 14 L18 1" fill="none" stroke="#1f5a9a" stroke-width="2.2"/></svg>You want to maximize rental property deductions</li>
  </ul>
  <ul class="reasons reasons-right">
    <li style="height:26px"><svg viewBox="0 0 19 16"><path d="M1 8 L7 14 L18 1" fill="none" stroke="#1f5a9a" stroke-width="2.2"/></svg>You’re a high-income earner and want to learn ways to pay less in taxes</li>
    <li style="height:26px"><svg viewBox="0 0 19 16"><path d="M1 8 L7 14 L18 1" fill="none" stroke="#1f5a9a" stroke-width="2.2"/></svg>You want to be represented by a tax expert before the FRB if you are subject to an audit</li>
    <li class="two-line"><svg viewBox="0 0 19 16"><path d="M1 8 L7 14 L18 1" fill="none" stroke="#1f5a9a" stroke-width="2.2"/></svg>You want to be updated periodically on tax law changes<br>and tax planning strategies</li>
  </ul>

  <section class="cta-band">
    <p class="references">REFERENCES AVAILABLE<br>UPON REQUEST</p>
    <div class="divider"></div>
    <p class="campaign">Would like to develop a marketing campaign that can be used periodically to digitally generate leads, build email contact list of prospective clients who want to receive tax update newsletters</p>
  </section>

  <footer class="footer"></footer>
  <div class="credential-badge" role="img" aria-label="Credential badge"></div>
  <div class="brand"><span class="brand-dot"></span><span class="brand-name">Pemberly &amp;<br>Associates LLC</span></div>
  <p class="services">Tax and Business Services</p>
  <p class="contact-line address"><svg viewBox="0 0 12 12"><path d="M6 0 A4 4 0 0 1 10 4 C10 7 6 12 6 12 C6 12 2 7 2 4 A4 4 0 0 1 6 0 Z M6 2.5 A1.5 1.5 0 1 0 6 5.5 A1.5 1.5 0 1 0 6 2.5 Z"/></svg>480 Harbor View Rd., Suite 210 Maple Falls, CA 95012</p>
  <p class="contact-line phone"><svg viewBox="0 0 12 12"><path d="M2.5 0.5 L4.5 3 L3.3 4.5 C4 6 5.8 7.9 7.5 8.7 L9 7.5 L11.5 9.5 L10 11.5 C5 11 1 7 0.5 2 Z"/></svg>(555) 014-2288</p>
  <p class="contact-line email"><svg viewBox="0 0 12 12"><path d="M0 2 H12 V10 H0 Z M0.8 2.6 L6 6.6 L11.2 2.6" stroke="#fff" stroke-width="0.8"/></svg>hello@pemberlytax.com</p>
</main>
</body>
</html>
```